Commercial HVAC and Refrigeration Business cards

Frost-Line Company is looking for flashy new business cards! We design, install, service and maintain commercial refrigeration, air conditioning, heating and refrigeration equipment. Our colors are blue and white. I'm open to single and double sided designs. Each employee will have their own business card. I've attached a copy of our current logo.

Our website, office and cell phone (cell phone is optional), email address should be clearly legible. "24 Hour Service" and the services we offer are; Sales, Service, Design, Installation, Maintenance. Refrigeration, Heating, Air Conditioning, Ice Machines. Does not have to be in any order.

Target Market(s)

Commercial; Restaurants, hotels, bars, breweries etc.

Industry/Entity Type

Hvac

Contact Information for Business Card

Name; Job Title, Phone Number, Email Address. www.frost-line-example.com 24 Hour Service. We provide - Sales, Design, Installation, Service, Maintenance. We service - Refrigeration, Heating, Air Conditioning, Ice Machines

Font styles to use
Other font styles liked:
• Be creative

Colors
0255a3
ffffff

Requirements
Must have
• Professional appearance and appeal to commercial clients in the food-service and hospitality industry. Must be clearly legible and easy to understand.
Nice to have
• We want to sell maintenance agreements, perhaps we can use the back of the card to tie into a webpage about our maintenance agreements.
Should not have
• Cartoons or unprofessional. Nothing too edgy.

```html
<!DOCTYPE html>
<html lang="en">
<head>
<meta charset="utf-8">
<title>Frost-Line Company – Business Card</title>
<link rel="stylesheet" href="https://fonts.googleapis.com/css2?family=Open+Sans:ital,wght@0,400;0,600;0,700;1,700&display=swap">
<style>
  :root {
    --brand-blue: #0a4282;
    --band-line: #c9ccd2;
    --white: #ffffff;
    --ink-grey: #5c5f66;
    --stage: #4b4b4b;
    --rule-grey: #b9bcc2;
  }
  * { box-sizing: border-box; margin: 0; padding: 0; }
  html, body {
    width: 1105px; height: 1200px; overflow: hidden;
    background: var(--stage);
    font-family: "Open Sans", Arial, sans-serif;
  }
  .canvas { position: relative; width: 1105px; height: 1200px; }

  .card {
    position: absolute; left: 196px; width: 720px; height: 412px;
    border-radius: 18px; overflow: hidden;
  }
  .card--front { top: 146px; background: var(--white); }
  .card--back { top: 602px; background: var(--brand-blue); color: var(--white); }

  .wordmark {
    position: absolute; left: 0; right: 0; text-align: center;
    font-weight: 600; font-size: 38px; letter-spacing: 0.2px; line-height: 1;
  }
  .card--front .wordmark { top: 118px; color: var(--brand-blue); }
  .card--back .wordmark { top: 140px; color: var(--white); }

  .holder {
    position: absolute; right: calc(720px - 301px); top: 236px; text-align: right;
  }
  .holder__name { font-weight: 600; font-size: 26px; color: var(--brand-blue); line-height: 1.2; }
  .holder__title { font-size: 19px; color: var(--ink-grey); line-height: 1.4; }

  .divider { position: absolute; left: 323px; top: 226px; width: 1px; height: 84px; background: var(--rule-grey); }

  .contacts { position: absolute; left: 350px; top: 226px; list-style: none; }
  .contacts li {
    display: flex; align-items: center; height: 27.5px;
    font-size: 19px; color: var(--ink-grey);
  }
  .contacts svg { width: 18px; height: 18px; margin-right: 10px; fill: var(--brand-blue); flex: none; }

  .service-band {
    position: absolute; left: 0; right: 0; bottom: 0; height: 46px;
    border-top: 4px solid var(--band-line);
    background: var(--brand-blue); color: var(--white);
    display: flex; align-items: center; justify-content: center;
    font-style: italic; font-weight: 700; font-size: 19px;
  }

  .agreements {
    position: absolute; left: 0; right: 0; top: 276px;
    display: flex; align-items: center; justify-content: center; gap: 6px;
    font-weight: 600; font-size: 23px;
  }
  .agreements::before, .agreements::after {
    content: ""; width: 130px; height: 1px;
  }
  .agreements::before { background: linear-gradient(to right, transparent, var(--white)); }
  .agreements::after { background: linear-gradient(to left, transparent, var(--white)); }

  .offer { position: absolute; left: 0; right: 0; text-align: center; font-size: 19px; white-space: nowrap; }
  .offer--provide { top: 320px; }
  .offer--service { top: 350px; }
  .offer__label { font-weight: 700; font-size: 22px; margin-right: 6px; }
</style>
</head>
<body>
<div class="canvas">

  <section class="card card--front" aria-label="Card front">
    <div class="wordmark">Frost-Line Company</div>

    <div class="holder">
      <div class="holder__name">Daniel Reyes</div>
      <div class="holder__title">CEO/Founder</div>
    </div>

    <div class="divider"></div>

    <ul class="contacts">
      <li>
        <svg viewBox="0 0 24 24" aria-hidden="true"><path d="M6.6 10.8a15.1 15.1 0 0 0 6.6 6.6l2.2-2.2a1 1 0 0 1 1-.25 11.4 11.4 0 0 0 3.6.57 1 1 0 0 1 1 1V20a1 1 0 0 1-1 1A17 17 0 0 1 3 4a1 1 0 0 1 1-1h3.5a1 1 0 0 1 1 1c0 1.25.2 2.45.57 3.6a1 1 0 0 1-.25 1z"/></svg>
        555 014 2368
      </li>
      <li>
        <svg viewBox="0 0 24 24" aria-hidden="true"><path d="M2 5h20v14H2z M3 6l9 7 9-7" fill="var(--brand-blue)"/><path d="M3.5 6.5l8.5 6.5 8.5-6.5" fill="none" stroke="#fff" stroke-width="1.6"/></svg>
        daniel@frost-line-example.com
      </li>
      <li>
        <svg viewBox="0 0 24 24" aria-hidden="true"><circle cx="12" cy="12" r="10"/><path d="M2 12h20M12 2c3 3 3 17 0 20M12 2c-3 3-3 17 0 20" fill="none" stroke="#fff" stroke-width="1.3"/></svg>
        www.frost-line-example.com
      </li>
    </ul>

    <div class="service-band">24 Hour Service.</div>
  </section>

  <section class="card card--back" aria-label="Card back">
    <div class="wordmark">Frost-Line Company</div>

    <div class="agreements">Maintenance agreements</div>

    <p class="offer offer--provide"><span class="offer__label">We provide :</span> Sales | Design | Installation | Service | Maintenance</p>
    <p class="offer offer--service"><span class="offer__label">We service :</span> Refrigeration | Heating | Air Conditioning | Ice Machines</p>
  </section>

</div>
</body>
</html>
```